Update the A4 Specials Page for Restaurant/Cafe

Provide a MINIMALIST attractive Specials page we can print weekly for our food and drink specials to give to our guests. Final design is to be provided in WORD Document so it can be easily edited by Manager. Should be black text and MINIMALIST to minimise ink usage as we print hundreds a week. We have UPLOADED the existing page as a template for you to update. Maybe logo can stay, see what you think. Or delete it and do something else. Keep it simple. Choose a good FONT. Could be a little playful with a cocktail ICON or something. Our existing menus can be seen at www.tallowmillcafe.com.au and they are using font Alegreya. Please note we are unable to provide any feedback to designers, however we really do appreciate your time if you are submitting a design. Thank you for your participation.

```html
<!DOCTYPE html>
<html lang="en">
<head>
<meta charset="utf-8">
<title>Weekly Specials – Tallow Mill Cafe</title>
<link href="https://fonts.googleapis.com/css2?family=Alegreya:ital,wght@0,400;0,500;0,800;0,900;1,400&display=swap" rel="stylesheet">
<style>
  :root {
    --backdrop: #4a4a4c;
    --paper: #f2f2f2;
    --ink: #111111;
    --ink-soft: #333333;
    --accent-blue: #2f4478;
    --brand-teal: #3f6a70;
    --frame: #8fa3a6;
    --ornament: #9a5a2c;
    --sketch-light: #d9d9d9;
    --sketch-dark: #a9a9a9;
  }
  * { margin: 0; padding: 0; box-sizing: border-box; }
  html, body {
    width: 1200px; height: 3359px; overflow: hidden;
    background: var(--backdrop);
    font-family: "Alegreya", Georgia, serif;
    color: var(--ink);
  }
  .specials-page {
    position: absolute; left: 150px; top: 1097px;
    width: 900px; height: 1164px;
    background: var(--paper);
  }
  .title-banner { position: absolute; left: 76px; top: 81px; width: 748px; height: 144px; }
  .title-ornament {
    position: absolute; left: 437px; top: 68px; width: 26px; height: 18px;
    background: var(--ornament); border-radius: 50% 50% 40% 40%;
  }
  .page-title {
    position: absolute; left: 0; right: 0; top: 108px;
    text-align: center; font-weight: 800; font-size: 68px; letter-spacing: 1px;
    line-height: 1;
  }
  .menu-item { position: absolute; left: 76px; }
  .item-name { font-weight: 800; font-size: 31px; line-height: 1; letter-spacing: .3px; }
  .item-price { position: absolute; top: 0; font-weight: 800; font-size: 30px; line-height: 1; }
  .item-feature { color: var(--accent-blue); font-size: 30px; line-height: 1; margin-top: 14px; }
  .item-desc { font-style: italic; font-size: 21px; color: var(--ink-soft); line-height: 1.45; margin-top: 10px; }
  .item-abv { position: absolute; font-style: italic; font-size: 21px; color: var(--accent-blue); }
  .cocktail-sketch {
    position: absolute; left: 594px; top: 411px; width: 306px; height: 724px;
    background: linear-gradient(180deg, var(--sketch-light), var(--sketch-dark) 60%, var(--sketch-light));
    border-radius: 150px 150px 20px 20px;
  }
  .cafe-name {
    position: absolute; left: 68px; top: 1022px; width: 260px;
    font-weight: 800; font-size: 34px; line-height: 1.05; color: var(--brand-teal);
    text-align: center;
  }
  .cafe-contact {
    position: absolute; left: 368px; top: 1022px;
    font-size: 23px; line-height: 1.2; color: var(--ink); font-style: normal;
  }
  .cafe-contact .web { margin-top: 12px; }
</style>
</head>
<body>
<main class="specials-page">
  <div class="title-ornament" role="img" aria-label="Small decorative flourish"></div>
  <svg class="title-banner" viewBox="0 0 748 144" aria-hidden="true">
    <g fill="none" stroke="var(--frame)" stroke-width="2">
      <polyline points="12,4 736,4 724,72 736,140 12,140 24,72 12,4"/>
      <polyline points="20,12 728,12 716,72 728,132 20,132 32,72 20,12"/>
    </g>
  </svg>
  <h1 class="page-title">WEEKLY SPECIALS</h1>

  <section class="menu-item" style="top:313px; width:560px;">
    <h2 class="item-name">CHICKEN FILO</h2>
    <span class="item-price" style="left:409px;">$24</span>
    <p class="item-desc">Creamy Chicken with Pinenuts, wrapped in Filo Pastry.<br>Served with Side Salad &amp; Zulu Sauce</p>
  </section>

  <section class="menu-item" style="top:476px; width:560px;">
    <h2 class="item-name">MINESTRONE SOUP</h2>
    <span class="item-price" style="left:429px;">$8</span>
    <p class="item-desc">Served with Garlic Bread</p>
  </section>

  <section class="menu-item" style="top:601px; width:560px;">
    <h2 class="item-name">COCKTAIL SPECIAL</h2>
    <span class="item-price" style="left:419px;">$17</span>
    <p class="item-feature">Golden Hour</p>
    <p class="item-desc" style="margin-top:18px;">Vodka, Passionfruit Pulp, Mango Puree<br>Top up with Ginger &amp; Lemon Kombucha</p>
  </section>

  <section class="menu-item" style="top:801px; width:560px;">
    <h2 class="item-name">CRAFT BEER SPECIAL</h2>
    <span class="item-price" style="left:409px;">$10</span>
    <p class="item-feature">Lucky Gecko</p>
    <p class="item-desc" style="margin-top:14px;">SUN HAZE, Tropical Pale Ale</p>
    <span class="item-abv" style="left:374px; top:84px;">4.8% Alc.</span>
  </section>

  <div class="cocktail-sketch" role="img" aria-label="Line sketch of a balloon cocktail glass with straw, fruit and ice"></div>

  <p class="cafe-name">TALLOW MILL<br>CAFE</p>
  <address class="cafe-contact">
    88 Harbour Road<br>Wirrina SA 5170
    <div class="web">tallowmillcafe.com.au</div>
  </address>
</main>
</body>
</html>
```